Palmova Dairy and Gluten Free Organic Ice Cream

Here is brief description regarding my project:

We a young Australian company who have started and created an innovative ice cream alternative. We have used organic coconut milk as the base mix of the ice cream and no sugar. Therefore our ice cream is healthy alternative for those who have intolerance also those who care about their well being.
Recently we just launched our ice cream with new formulation as well as new packaging. We have an existing website www.palmova.com.au which needs to be improved greatly to incorporate a more organic and fresh looks. We would like to make it visually attractive and entice visitors to engage more. Please check our existing website.
We also like a new young generation design and creative without losing the core purpose of telling audience that our products are natural, organic and healthy.

Please email rubek@palmova.com.au to request more files if required.

Target Market(s)

Health conscious people, organic, natural food, sugar free people

Industry/Entity Type

It Company

Number of Pages Required

4 page

Font styles to use
Other font styles liked:
• Please check Palmova's website www.palmova.com.au

Requirements
Must have
• The products pictures which are our ice cream tubs. We have 10 flavours in total.
• Inclusion of fresh coconut with splash of coconut milk, fruits, etc which represent the ice cream flavours (10 flavours).
• Please see links below for favourite websites. Since we have 10 flavours hence it would be good if we could have each ice cream flavour with its descrption etc.
• Favourite 1:
• https://www.vantelo.com/#/products/grain-vigour
• Favourite 2:
• https://www.pixlora.net/gallery/ORCHARD-BASKET/48215096
• Favourite 3:
• http://www.brivel.co.uk/
Nice to have
• Organic background

```html
<!DOCTYPE html>
<html lang="en">
<head>
<meta charset="utf-8">
<title>Palmova — Dairy &amp; Gluten Free Ice Cream</title>
<link href="https://fonts.googleapis.com/css2?family=Open+Sans:wght@300;400;700&family=Yanone+Kaffeesatz:wght@400&family=Yesteryear&display=swap" rel="stylesheet">
<style>
:root{
  --wood:#6e5040;
  --wood-dark:#4e3728;
  --ink:#2b2522;
  --yellow:#ffcc00;
  --white:#ffffff;
  --text:#222222;
  --sky:#5fa5e6;
  --sky-light:#a9cfee;
}
*{box-sizing:border-box;margin:0;padding:0}
html,body{width:760px;height:1200px;overflow:hidden}
body{position:relative;font-family:"Open Sans",Arial,sans-serif;color:var(--text);background:var(--wood)}
.abs{position:absolute}
.wood-bg{left:0;top:0;width:760px;height:1200px;background:linear-gradient(135deg,#7a5a45,var(--wood) 50%,#5e4434)}
.header{left:0;top:0;width:760px;height:76px;background:var(--ink)}
.logo-box{left:131px;top:0;width:96px;height:76px;background:var(--white);display:flex;flex-direction:column;align-items:center;justify-content:center}
.logo-name{font-family:"Open Sans",sans-serif;font-weight:300;font-size:17px;letter-spacing:1px;color:var(--ink);line-height:20px}
.logo-tag{font-size:4.8px;color:var(--ink);margin-top:3px;white-space:nowrap;letter-spacing:.1px}
.nav{top:58px;left:311px;font-size:7.5px;font-weight:300;color:var(--yellow);text-transform:uppercase}
.nav span{position:absolute;white-space:nowrap}
.social{width:7px;height:7px;background:var(--yellow);top:59px}
.dropdown{left:437px;top:76px;width:98px;height:55px;background:var(--ink)}
.dropdown a{position:absolute;left:8px;font-size:5px;color:var(--yellow);text-decoration:none}
.dropdown i{position:absolute;left:8px;width:84px;border-top:1px dashed var(--yellow)}
.caret{left:448px;top:67px;width:0;height:0;border-left:3px solid transparent;border-right:3px solid transparent;border-top:4px solid var(--yellow)}
.page{left:131px;top:76px;width:497px;height:1030px;background:var(--white)}
.hero-photo{left:131px;top:77px;width:497px;height:313px;background:linear-gradient(180deg,var(--sky),var(--sky-light))}
.hero-curve{left:131px;top:320px}
.arrow{width:12px;height:36px;background:var(--yellow);top:196px}
.arrow svg{display:block;margin:14px auto 0}
.hero-title{left:276px;top:156px;font-family:"Yanone Kaffeesatz",sans-serif;font-size:40px;line-height:36px;color:var(--white)}
.hero-rule{left:277px;top:236px;width:86px;height:3px;background:var(--ink)}
.hero-tubs{left:400px;top:128px;width:186px;height:122px;border-radius:12px;background:linear-gradient(90deg,#7a4a2e,#d9a52c,#f0a23a)}
.hero-sub{left:281px;top:276px;font-size:7px;font-weight:700;color:var(--ink);white-space:nowrap}
.btn{left:351px;top:288px;width:69px;height:22px;background:var(--ink);color:var(--yellow);font-size:6.5px;font-weight:700;display:flex;align-items:center;justify-content:center}
.yellow-band{left:131px;top:388px;width:497px;height:56px;background:var(--yellow)}
.script{font-family:"Yesteryear",cursive;font-weight:400;color:var(--ink);text-align:center;width:497px;left:131px}
.dash{left:131px;width:497px;border-top:1px dashed var(--ink)}
.copy{font-size:5.6px;line-height:7.2px;color:var(--text)}
.feature{width:107px;height:42px;border:1px solid var(--ink);background:var(--white);font-size:6.5px;font-weight:700;display:flex;align-items:center;color:var(--ink)}
.plus{position:absolute;width:10px;height:10px}
.tooltip{background:var(--ink);color:var(--white);font-size:4px;line-height:5px;padding:3px 4px;width:80px}
.tub-hero{left:305px;top:514px;width:160px;height:188px;border-radius:10px 10px 30px 30px;background:linear-gradient(180deg,#f2f2f2 0%,#9fd0f0 20%,#7bbde6 100%)}
.about-band{left:131px;top:828px;width:497px;height:272px;background:var(--yellow)}
.about-copy{left:189px;top:840px;width:198px;font-size:5.6px;line-height:7.2px;color:var(--ink)}
.about-copy p{margin-bottom:6px}
.about-photo{left:397px;top:841px;width:181px;height:121px;background:linear-gradient(90deg,#b68f7a,#c8c2b8 55%,#9fb4c6)}
.tub{border-radius:8px 8px 16px 16px}
.footer{left:0;top:1106px;width:760px;height:94px;background:var(--ink)}
.footer-logo{left:131px;top:1110px;width:94px;height:66px;background:var(--white);display:flex;flex-direction:column;align-items:center;justify-content:center}
.f-head{font-family:"Yesteryear",cursive;font-weight:400;color:var(--yellow);font-size:12px;top:1115px}
.f-link{font-size:5.2px;color:var(--yellow);line-height:10px;white-space:nowrap}
.legal{left:0;top:1181px;width:760px;text-align:center;font-size:4px;color:#cfc7bf}
</style>
</head>
<body>
<div class="abs wood-bg" role="img" aria-label="Weathered dark timber planks laid diagonally"></div>

<header class="abs header"></header>
<div class="abs logo-box"><span class="logo-name">PALMOVA</span><span class="logo-tag">DAIRY &amp; GLUTEN FREE ICE CREAM</span></div>
<nav class="abs nav">
  <span style="left:0">Home</span>
  <span style="left:44px">Our Ice Creams</span>
  <span style="left:129px">Info</span>
  <span style="left:173px">About Us</span>
  <span style="left:231px">Contact Us</span>
</nav>
<div class="abs social" style="left:604px"></div>
<div class="abs social" style="left:612px"></div>
<div class="abs caret"></div>

<div class="abs page"></div>
<div class="abs hero-photo" role="img" aria-label="Photo of a child doing a handstand on grass under a blue sky"></div>
<svg class="abs hero-curve" width="497" height="70" viewBox="0 0 497 70"><path d="M0 20 Q250 100 497 14 L497 70 L0 70 Z" fill="#ffcc00"/></svg>
<div class="abs arrow" style="left:131px"><svg width="8" height="8" viewBox="0 0 8 8"><path d="M6 1 L2 4 L6 7" stroke="#fff" stroke-width="1.5" fill="none"/></svg></div>
<div class="abs arrow" style="left:616px"><svg width="8" height="8" viewBox="0 0 8 8"><path d="M2 1 L6 4 L2 7" stroke="#fff" stroke-width="1.5" fill="none"/></svg></div>
<div class="abs hero-title">AMAZING<br>TASTES!</div>
<div class="abs hero-rule"></div>
<div class="abs hero-tubs" role="img" aria-label="Three ice cream tubs: chocolate, iced coffee and mango"></div>
<div class="abs hero-sub">TASTE OUR 10 AMAZING DAIRY &amp; GLUTEN FREE ICE CREAM</div>
<div class="abs btn">OUR ICE CREAMS</div>

<div class="abs dropdown">
  <a style="top:4px">NEWS</a><i style="top:14px"></i>
  <a style="top:17px">HEALTH FACTS</a><i style="top:27px"></i>
  <a style="top:30px">WHAT'S ON</a><i style="top:40px"></i>
  <a style="top:44px">STOCKISTS</a>
</div>

<div class="abs yellow-band"></div>
<h2 class="abs script" style="top:415px;font-size:20px;line-height:26px">Why our creams ?</h2>
<div class="abs dash" style="top:444px"></div>
<p class="abs copy" style="left:244px;top:450px;width:272px;text-align:justify">Lorem ipsum dolor sit amet, consectetur adipiscing elit. Aenean turpis nibh, lacinia vel massa in, pharetra tincidunt libero. Nullam eu urna varius nulla viverra ornare. Pellentesque quis pharetra dui, a consequat risus. Donec ligula mi, bibendum in malesuada nec, adipiscing eget purus. Lorem ipsum dolor sit amet, consectetur adipiscing elit. Duis vel molestie mi, sit amet convallis turpis. Quisque egestas volutpat ligula, et cursus erat imperdiet non. Vivamus mollis enim non tincidunt malesuada.</p>

<div class="abs feature" style="left:161px;top:519px;padding-left:9px">GLUTEN FREE<svg class="plus" style="left:90px;top:15px" viewBox="0 0 10 10"><circle cx="5" cy="5" r="4.3" fill="none" stroke="#2b2522"/><path d="M5 2.5V7.5M2.5 5H7.5" stroke="#2b2522"/></svg></div>
<div class="abs feature" style="left:161px;top:585px;padding-left:9px">DAIRY FREE<svg class="plus" style="left:90px;top:15px" viewBox="0 0 10 10"><circle cx="5" cy="5" r="4.3" fill="none" stroke="#2b2522"/><path d="M5 2.5V7.5M2.5 5H7.5" stroke="#2b2522"/></svg></div>
<div class="abs feature" style="left:161px;top:650px;padding-left:9px">FRUCTOSE FRIENDLY<svg class="plus" style="left:90px;top:15px" viewBox="0 0 10 10"><circle cx="5" cy="5" r="4.3" fill="none" stroke="#2b2522"/><path d="M5 2.5V7.5M2.5 5H7.5" stroke="#2b2522"/></svg></div>
<div class="abs feature" style="left:496px;top:519px;padding-left:40px"><svg class="plus" style="left:9px;top:15px" viewBox="0 0 10 10"><circle cx="5" cy="5" r="4.3" fill="none" stroke="#2b2522"/><path d="M5 2.5V7.5M2.5 5H7.5" stroke="#2b2522"/></svg>VEGAN FRIENDLY</div>
<div class="abs feature" style="left:496px;top:585px;padding-left:31px"><svg class="plus" style="left:9px;top:15px" viewBox="0 0 10 10"><circle cx="5" cy="5" r="4.3" fill="none" stroke="#2b2522"/><path d="M5 2.5V7.5M2.5 5H7.5" stroke="#2b2522"/></svg>CERTIFIED ORGANIC</div>
<div class="abs feature" style="left:496px;top:650px;padding-left:40px"><svg class="plus" style="left:9px;top:15px" viewBox="0 0 10 10"><circle cx="5" cy="5" r="4.3" fill="none" stroke="#2b2522"/><path d="M5 2.5V7.5M2.5 5H7.5" stroke="#2b2522"/></svg>10 GREAT TASTES</div>
<div class="abs tooltip" style="left:245px;top:499px">Free from gluten, made with organic coconut milk and no added sugar, so everyone at the table can share a scoop without worry.</div>
<div class="abs tub-hero" role="img" aria-label="Large choc coconut ice cream tub"></div>

<h2 class="abs script" style="top:754px;font-size:20px;line-height:26px">About Us ?</h2>
<div class="abs dash" style="top:784px"></div>
<p class="abs copy" style="left:244px;top:788px;width:272px">Pellentesque dictum vulputate sem quis feugiat. In tristique tellus id mauris lacinia, vel eleifend lorem sollicitudin.<br>Maecenas volutpat mauris vel metus gravida aliquet. Cum sociis natoque penatibus et magnis dis parturient montes, nascetur ridiculus mus. Interdum et malesuada fames ac ante ipsum primis in faucibus. Mauris vitae lorem eget nulla pretium luctus quis nec urna. Fusce pharetra iaculis mauris.</p>

<section class="abs about-band"></section>
<div class="abs about-copy">
  <p>Palmova was founded by Mara Wendt when she first discovered the benefits of coconuts through her passion for healthy living and healthy eating.</p>
  <p>Surrounded by family and friends with dairy and gluten sensitivities, she searched the supermarkets unsuccessfully for healthy alternative frozen desserts that were pure, tasty, natural and certified organic.</p>
  <p>This led Mara to develop a dessert that could deliver all the benefits and none of the disadvantages of so many other products.</p>
  <p>Mara and her husband Theo, head a team of innovative organic food technologists, manufacturers and natural health food distributors. They source, blend and manufacture the purest ingredients for Palmova's ice cream from fully certified organic suppliers and growers around the world and in Australia.</p>
  <p>Palmova products are Australian, made in Melbourne.</p>
</div>
<div class="abs about-photo" role="img" aria-label="Photo of the founding couple on a city street"></div>

<div class="abs tub" style="left:182px;top:1007px;width:42px;height:54px;background:#9ccc3c" role="img" aria-label="Lime ice cream tub"></div>
<div class="abs tub" style="left:227px;top:1007px;width:42px;height:54px;background:#f0922a" role="img" aria-label="Orange ice cream tub"></div>
<div class="abs tub" style="left:271px;top:1007px;width:42px;height:54px;background:#c9a23c" role="img" aria-label="Caramel ice cream tub"></div>
<div class="abs tub" style="left:315px;top:1007px;width:42px;height:54px;background:#8c5a36" role="img" aria-label="Chocolate ice cream tub"></div>
<div class="abs tub" style="left:359px;top:1007px;width:36px;height:54px;background:#3c8fd8" role="img" aria-label="Blue coconut ice cream tub"></div>
<div class="abs tub" style="left:389px;top:993px;width:70px;height:82px;background:#b0462a" role="img" aria-label="Featured berry ice cream tub"></div>
<div class="abs tub" style="left:452px;top:1007px;width:38px;height:54px;background:#ee8a3a" role="img" aria-label="Mango ice cream tub"></div>
<div class="abs tub" style="left:491px;top:1007px;width:42px;height:54px;background:#e2bb3a" role="img" aria-label="Iced coffee ice cream tub"></div>
<div class="abs tub" style="left:536px;top:1007px;width:42px;height:54px;background:#a9d2ee" role="img" aria-label="Choc coconut ice cream tub"></div>
<div class="abs tooltip" style="left:412px;top:977px;background:#b0462a;width:80px">Wild berries swirled through creamy coconut, naturally sweet and fully organic.</div>
<div class="abs dash" style="top:1100px;border-color:#fff"></div>

<footer class="abs footer"></footer>
<div class="abs footer-logo"><span class="logo-name">PALMOVA</span><span class="logo-tag">DAIRY &amp; GLUTEN FREE ICE CREAM</span></div>
<h3 class="abs f-head" style="left:240px">Navigation</h3>
<h3 class="abs f-head" style="left:340px">Information</h3>
<h3 class="abs f-head" style="left:432px">Contact Us</h3>
<div class="abs f-link" style="left:240px;top:1135px">HOME<br>OUR ICE CREAMS<br>ABOUT US</div>
<div class="abs f-link" style="left:340px;top:1135px">NEWS<br>HEALTH FACTS<br>WHAT'S ON<br>STOCKISTS</div>
<div class="abs f-link" style="left:432px;top:1135px">ADRESS LINE INFORMATION<br>ADRESS LINE INFORMATION<br>TELEPHONE NUMBER</div>
<div class="abs social" style="left:432px;top:1166px"></div>
<div class="abs social" style="left:441px;top:1166px"></div>
<div class="abs legal">2015 © Palmova Ice Creams · All Rights Reserved · Privacy Policy</div>
</body>
</html>
```